Higher co-efficient of performance means more heat for your money

I need a bar graph that will have the following heating systems, 80% efficient gas furnace COP of .8, Electric heat COP of 1, and Our best selling heat pump with a cop of 4 at 47F. I will have a constant bar, 100$ worth of gas for furnace, 100$ of electricity for electric heat, and 100$ worth of electricity for our heat pumps. next to them I will have a bar showing how much heat each heating system will provide for $100 of fuel. For gas furnace I need a bar that says $80 worth of heat and the barograph to match it, for electric heat I need the bar to show 100$ worth of heat, for our best selling heat pump I need the bar graph to show and say $400 dollars worth of heat. Please take a look at my website www.brightmarkcomfort.example for brand color and feel

```html
<!DOCTYPE html>
<html lang="en">
<head>
<meta charset="utf-8">
<title>Brightmark Comfort – More Heat for Your Money</title>
<link href="https://fonts.googleapis.com/css2?family=Exo:wght@500;600&family=Oswald:wght@600&display=swap" rel="stylesheet">
<style>
  :root {
    --brand-blue: #0f6db5;
    --panel-white: #ffffff;
    --stripe-blue: #a9cdea;
    --bar-dark: #8a0b14;
    --bar-light: #d9497c;
    --bar-pale: #e9a3b3;
    --ink: #0b0b0b;
    --brand-red: #c4202b;
  }
  * { margin: 0; padding: 0; box-sizing: border-box; }
  html, body { width: 927px; height: 1200px; overflow: hidden; background: var(--brand-blue); }
  .poster {
    position: relative; width: 927px; height: 1200px;
    background: var(--brand-blue);
    font-family: "Exo", sans-serif;
  }
  .panel {
    position: absolute; left: 71px; top: 0; width: 856px; height: 1045px;
    background: var(--panel-white);
  }
  .panel-rule-v {
    position: absolute; left: 79px; top: 0; width: 4px; height: 1036px;
    background: var(--brand-blue);
  }
  .panel-rule-h {
    position: absolute; left: 79px; top: 1032px; width: 848px; height: 4px;
    background: var(--brand-blue);
  }
  .brand {
    position: absolute; left: 505px; top: 110px; width: 380px;
    display: flex; flex-direction: column; align-items: center; gap: 22px;
  }
  .brand-mark {
    width: 96px; height: 96px; border-radius: 50%;
    background: var(--brand-red);
  }
  .brand-name {
    font-family: "Exo", sans-serif; font-weight: 600;
    font-size: 42px; color: var(--brand-blue); letter-spacing: 1px;
    white-space: nowrap;
  }
  .headline {
    position: absolute; right: 212px; top: 372px;
    text-align: right; color: var(--ink);
    font-weight: 500; font-size: 51px; line-height: 57px;
    letter-spacing: 0.5px;
  }
  .footnote {
    position: absolute; left: 112px; top: 616px;
    color: var(--ink); font-weight: 500; font-size: 72px; line-height: 1;
    letter-spacing: 1px;
  }
  .chart {
    position: absolute; left: 86px; top: 360px; width: 841px; height: 672px;
  }
  .axis-label {
    position: absolute; left: 20px; top: 935px;
    transform: rotate(-90deg); transform-origin: center;
    color: var(--panel-white); font-family: "Oswald", sans-serif;
    font-weight: 600; font-size: 19px; letter-spacing: 2px; white-space: nowrap;
  }
  .category {
    position: absolute; color: var(--panel-white);
    font-weight: 500; line-height: 1.1;
  }
  .category--furnace { left: 178px; top: 1069px; font-size: 20px; }
  .category--electric { left: 408px; top: 1094px; font-size: 20px; }
  .category--heatpump { left: 645px; top: 1068px; text-align: center; }
  .category--heatpump .small { display: block; font-size: 17px; }
  .category--heatpump .large { display: block; font-size: 23px; }
</style>
</head>
<body>
<main class="poster">
  <div class="panel"></div>

  <svg class="chart" viewBox="0 0 841 672" aria-hidden="true">
    <defs>
      <linearGradient id="bar-fill" x1="0" y1="0" x2="0" y2="1">
        <stop offset="0" stop-color="var(--bar-dark)"/>
        <stop offset="1" stop-color="var(--bar-light)"/>
      </linearGradient>
      <linearGradient id="bar-fill-tall" x1="0" y1="0" x2="0" y2="1">
        <stop offset="0" stop-color="var(--bar-dark)"/>
        <stop offset="0.55" stop-color="var(--bar-light)"/>
        <stop offset="1" stop-color="var(--bar-pale)"/>
      </linearGradient>
    </defs>
    <g class="gridlines" fill="var(--stripe-blue)">
      <rect x="0" y="510" width="841" height="4"/>
      <rect x="0" y="522" width="841" height="4"/>
      <rect x="0" y="534" width="841" height="4"/>
      <rect x="0" y="546" width="841" height="4"/>
      <rect x="0" y="558" width="841" height="4"/>
      <rect x="0" y="570" width="841" height="4"/>
      <rect x="0" y="582" width="841" height="4"/>
      <rect x="0" y="594" width="841" height="4"/>
      <rect x="0" y="606" width="841" height="4"/>
      <rect x="0" y="618" width="841" height="4"/>
      <rect x="0" y="630" width="841" height="4"/>
      <rect x="0" y="642" width="841" height="4"/>
      <rect x="0" y="654" width="841" height="4"/>
    </g>
    <g class="bars">
      <rect class="bar bar--furnace-cost" x="96" y="508" width="68" height="164" fill="url(#bar-fill)"/>
      <rect class="bar bar--furnace-heat" x="182" y="541" width="68" height="131" fill="url(#bar-fill)"/>
      <rect class="bar bar--electric-cost" x="328" y="508" width="68" height="164" fill="url(#bar-fill)"/>
      <rect class="bar bar--electric-heat" x="414" y="508" width="68" height="164" fill="url(#bar-fill)"/>
      <rect class="bar bar--heatpump-cost" x="564" y="508" width="68" height="164" fill="url(#bar-fill)"/>
      <rect class="bar bar--heatpump-heat" x="652" y="10" width="68" height="662" fill="url(#bar-fill-tall)"/>
    </g>
  </svg>

  <div class="panel-rule-v"></div>
  <div class="panel-rule-h"></div>

  <div class="brand">
    <div class="brand-mark"></div>
    <div class="brand-name">Brightmark Comfort</div>
  </div>

  <h1 class="headline">Higher Co-efficient<br>of Performance<br>means moreheat<br>for your money</h1>
  <p class="footnote">* COP ad 47° F</p>

  <span class="axis-label">$ 100</span>

  <p class="category category--furnace">80%<br>gas Furnace</p>
  <p class="category category--electric">Electric Heat</p>
  <p class="category category--heatpump"><span class="small">Our Best Selling</span><span class="large">Heat Pump</span></p>
</main>
</body>
</html>
```